T.K.R.A.C. Soccer Tryouts 2015-2016

I am looking for a soccer tryout flyer that stands out and catches peoples attention. An emphasis can be put on the cost, since we are by far the lowest cost program in the area. Below are the details for the flyer. I have also attached the club logo and pictures that can be used if needed.

T.K.R.A.C. SOCCER TRYOUTS
2015-2016

Club Fee: $699.00 per player

Tryout Schedule

Boys ages U9 through U14
Weds. May 27th and Friday May 29th
6:00 pm - 8:00 pm

Girls ages U9 through U14
Tuesday May 26th and Thursday May 28th
6:00 pm - 8:00 pm

All tryouts will be held at PLOV Fields
(Next to Gritmark Hardware factory at the corner of Rt. 342 and Hollow Brook Road)

We are encouraging all players to pre-register

Same Day Registrations will begin at 5:30

All players should bring a properly inflated ball, shin guards and water.

In the event of inclement weather, the tryouts will be moved to the JET indoor facility located at 4827 Dunmore Lane in Fernwood Lake. The scheduled time slots will remain the same.

Website: www.tkracsoccer-example.com

Target Market(s)

Youth Soccer

Requirements
Must have
• Logo

```html
<!DOCTYPE html>
<html lang="en">
<head>
<meta charset="utf-8">
<title>T.K.R.A.C. Soccer Tryouts 2015-2016</title>
<link rel="stylesheet" href="https://fonts.googleapis.com/css2?family=Anton&family=Oswald:wght@400;500;700&display=swap">
<style>
  :root {
    --deep-green: #0b2a12;
    --pitch-green: #17501f;
    --bright-green: #7fd13b;
    --lime: #b6f04a;
    --white: #ffffff;
    --panel: #08160b;
    --shadow: rgba(0,0,0,0.6);
  }
  html, body {
    margin: 0;
    padding: 0;
    overflow: hidden;
  }
  body {
    width: 816px;
    height: 1200px;
    background: #222;
  }
  .flyer {
    position: relative;
    width: 816px;
    height: 1200px;
    overflow: hidden;
    background: radial-gradient(ellipse at 50% 45%, var(--pitch-green) 0%, var(--deep-green) 70%, #051509 100%);
    font-family: "Oswald", sans-serif;
    color: var(--white);
    text-align: center;
  }
  .team-photo {
    position: absolute;
    left: 0; top: 0;
    width: 816px; height: 330px;
    background: linear-gradient(180deg, #2c3a30 0%, #1e3a22 55%, #123016 100%);
  }
  .team-photo::after {
    content: "";
    position: absolute;
    left: 0; right: 0; bottom: 0; height: 90px;
    background: linear-gradient(180deg, rgba(11,42,18,0) 0%, var(--deep-green) 100%);
  }
  .club-mark {
    position: absolute;
    top: 60px; left: 0; right: 0;
    display: flex;
    flex-direction: column;
    align-items: center;
    gap: 12px;
    z-index: 2;
  }
  .club-mark__dot {
    width: 120px; height: 120px;
    border-radius: 50%;
    background: var(--pitch-green);
  }
  .club-mark__name {
    font-family: "Anton", sans-serif;
    font-size: 30px;
    color: var(--white);
    letter-spacing: 2px;
  }
  .headline {
    position: absolute;
    left: 0; right: 0;
    margin: 0;
    font-family: "Anton", sans-serif;
    line-height: 1;
    text-shadow: 0 3px 6px var(--shadow);
  }
  .headline--club { top: 335px; font-size: 48px; letter-spacing: 2px; }
  .headline--title { top: 390px; font-size: 70px; color: var(--bright-green); letter-spacing: 1px; }
  .headline--season { top: 468px; font-size: 58px; font-style: italic; }
  .headline--fee { top: 534px; font-size: 50px; }
  .headline--per { top: 588px; font-size: 30px; }

  .schedule {
    position: absolute;
    left: 90px; top: 632px;
    width: 636px; height: 140px;
    background: var(--panel);
    border: 2px solid var(--bright-green);
  }
  .schedule__header {
    background: var(--bright-green);
    color: var(--deep-green);
    font-family: "Anton", sans-serif;
    font-size: 28px;
    line-height: 40px;
    letter-spacing: 1px;
  }
  .schedule__cols {
    display: flex;
    height: 100px;
  }
  .schedule__group {
    flex: 1;
    display: flex;
    flex-direction: column;
    justify-content: center;
    font-weight: 700;
    font-size: 19px;
    line-height: 1.2;
    text-transform: uppercase;
  }
  .schedule__group + .schedule__group { border-left: 2px solid var(--bright-green); }
  .schedule__group-title { color: var(--lime); font-size: 21px; }

  .details {
    position: absolute;
    left: 40px; right: 40px;
    margin: 0;
    text-transform: uppercase;
    font-weight: 700;
    line-height: 1.2;
  }
  .details--venue { top: 784px; font-size: 22px; color: var(--lime); }
  .details--venue-note { top: 812px; font-size: 15px; font-weight: 500; }
  .details--prereg { top: 840px; font-size: 22px; }
  .details--sameday { top: 868px; font-size: 20px; color: var(--lime); }
  .details--bring { top: 904px; font-size: 26px; font-family: "Anton", sans-serif; font-weight: 400; line-height: 1.15; }
  .details--weather { top: 975px; font-size: 13px; font-weight: 400; line-height: 1.35; color: var(--lime); }

  .website {
    position: absolute;
    left: 0; right: 0; top: 1062px;
    height: 62px;
    background: linear-gradient(90deg, rgba(127,209,59,0) 0%, var(--bright-green) 25%, var(--bright-green) 75%, rgba(127,209,59,0) 100%);
    color: var(--deep-green);
    font-family: "Anton", sans-serif;
    font-size: 36px;
    line-height: 62px;
    letter-spacing: 2px;
  }
</style>
</head>
<body>
  <main class="flyer">
    <div class="team-photo" role="img" aria-label="Team photo of youth soccer players in club kits"></div>
    <div class="club-mark">
      <span class="club-mark__dot"></span>
      <span class="club-mark__name">T.K.R.A.C.</span>
    </div>

    <h2 class="headline headline--club">T.K.R.A.C.</h2>
    <h1 class="headline headline--title">SOCCER TRYOUTS</h1>
    <p class="headline headline--season">2015-2016</p>
    <p class="headline headline--fee">CLUB FEE: $699.00</p>
    <p class="headline headline--per">PER PLAYER</p>

    <section class="schedule">
      <div class="schedule__header">TRYOUT SCHEDULE</div>
      <div class="schedule__cols">
        <div class="schedule__group">
          <span class="schedule__group-title">Boys ages U9 through U14</span>
          <span>Weds. May 27th and</span>
          <span>Friday May 29th</span>
          <span>6:00 pm - 8:00 pm</span>
        </div>
        <div class="schedule__group">
          <span class="schedule__group-title">Girls ages U9 through U14</span>
          <span>Tuesday May 26th and</span>
          <span>Thursday May 28th</span>
          <span>6:00 pm - 8:00 pm</span>
        </div>
      </div>
    </section>

    <p class="details details--venue">All tryouts will be held at PLOV Fields</p>
    <p class="details details--venue-note">(Next to Gritmark Hardware factory at the corner of Rt. 342 and Hollow Brook Road)</p>
    <p class="details details--prereg">We are encouraging all players to pre-register</p>
    <p class="details details--sameday">Same day registrations will begin at 5:30</p>
    <p class="details details--bring">All players should bring a properly<br>inflated ball, shin guards and water.</p>
    <p class="details details--weather">In the event of inclement weather, the tryouts will be moved to the JET indoor facility located<br>at 4827 Dunmore Lane in Fernwood Lake. The scheduled time slots will remain the same.</p>

    <div class="website">WWW.TKRACSOCCER-EXAMPLE.COM</div>
  </main>
</body>
</html>
```